New customer flyer

Looking for a flyer that can be written on as a field estimate for door to door sales
Ideally have some nice on the front with the back as a estimate form
Doorknob hanger size

Target Market(s)

Home owners buying core aeration service

Industry/Entity Type

Lawn Care

Requirements
Must have
• Logo
• First name
• Last name
• Cell
• Email
• Address
• Sq ft
Nice to have
• Benefits of core aeration

```html
<!DOCTYPE html>
<html lang="en">
<head>
<meta charset="UTF-8">
<title>GreenCore Door Hanger</title>
<link href="https://fonts.googleapis.com/css2?family=Montserrat:wght@500;600;700;800;900&family=Open+Sans:wght@400;600&display=swap" rel="stylesheet">
<style>
:root{
  --bg:#e9e9e9;
  --green-dark:#17792f;
  --green:#2f9a3b;
  --green-light:#8cc63f;
  --lime:#9acd32;
  --blue:#2c4f9e;
  --blue-deep:#1e3f8a;
  --ink:#1f2a33;
  --white:#ffffff;
  --line:#b9c2b9;
}
*{box-sizing:border-box;margin:0;padding:0}
html,body{width:1200px;height:2776px;overflow:hidden;background:var(--bg)}
body{position:relative;font-family:'Open Sans',sans-serif}
.hanger{position:absolute;top:702px;width:520px;height:1372px;overflow:hidden;box-shadow:0 6px 18px rgba(0,0,0,.18)}
.hanger--front{left:50px;background:var(--white)}
.hanger--back{left:630px;background:var(--green)}
.hanger__hole{position:absolute;left:190px;top:40px;width:140px;height:140px;border-radius:50%;background:var(--bg);z-index:5}
.layer{position:absolute;left:0;top:0}

/* front */
.front__brand{position:absolute;top:730px;left:0;width:100%;display:flex;justify-content:center;align-items:center;gap:12px}
.front__brand-dot{width:34px;height:34px;border-radius:50%;background:var(--blue)}
.front__brand-name{font-family:'Montserrat',sans-serif;font-weight:800;font-size:44px;color:var(--blue);letter-spacing:-.5px}
.front__headline{position:absolute;top:800px;width:100%;text-align:center;font-family:'Montserrat',sans-serif;text-transform:uppercase}
.front__make{font-weight:900;font-size:118px;line-height:1;color:var(--ink)}
.front__garden{font-weight:700;font-size:54px;line-height:1.15;color:var(--lime)}
.front__paradise{font-weight:700;font-size:48px;line-height:1.1;color:var(--ink)}
.call-pill{position:absolute;left:30px;width:460px;height:62px;border-radius:10px;display:flex;align-items:center;justify-content:center;font-family:'Montserrat',sans-serif;font-weight:700;font-size:34px;color:var(--white);text-transform:uppercase}
.front .call-pill,.hanger--front .call-pill{top:1088px;background:var(--blue)}
.phone{position:absolute;width:100%;text-align:center;font-family:'Montserrat',sans-serif;font-weight:800;font-size:68px;letter-spacing:1px}
.hanger--front .phone{top:1160px;color:var(--ink)}

/* back */
.back__photo{position:absolute;inset:0;background:linear-gradient(180deg,#2f8f3a 0%,#3da33f 40%,#5bb34a 70%,#7fa66b 100%)}
.back__title{position:absolute;top:250px;width:100%;text-align:center;font-family:'Montserrat',sans-serif;font-weight:700;font-size:40px;color:var(--white)}
.benefits{position:absolute;top:320px;left:58px;right:30px;list-style:none}
.benefits li{display:flex;align-items:flex-start;gap:14px;color:var(--white);font-size:21px;line-height:1.25;margin-bottom:16px;font-weight:600}
.benefits svg{flex:none;width:28px;height:28px}
.back__prompt{position:absolute;top:640px;width:100%;text-align:center;font-family:'Montserrat',sans-serif;font-weight:700;color:var(--white)}
.back__prompt-lead{font-size:30px}
.back__prompt-strong{font-size:40px;font-weight:900;text-transform:uppercase}
.form-box{position:absolute;top:760px;left:150px;width:330px;height:400px;background:var(--white);border-radius:8px;padding:30px 22px}
.form-row{display:flex;align-items:flex-end;height:56px;font-size:19px;color:var(--ink)}
.form-row span{white-space:nowrap;margin-right:10px}
.form-row i{flex:1;border-bottom:1.5px solid var(--line);height:1px}
.hanger--back .call-pill{top:1182px;background:var(--green-dark)}
.hanger--back .phone{top:1246px;color:var(--white)}
.back__band{position:absolute;left:0;bottom:0;width:100%;height:42px;background:var(--blue-deep)}
</style>
</head>
<body>

<section class="hanger hanger--front">
  <div class="hanger__hole"></div>
  <svg class="layer" width="520" height="1372" viewBox="0 0 520 1372">
    <defs>
      <linearGradient id="front-top" x1="0" y1="0" x2="0" y2="1">
        <stop offset="0" stop-color="#1f8a33"/>
        <stop offset="1" stop-color="#126c28"/>
      </linearGradient>
    </defs>
    <polygon points="0,0 520,0 520,560 260,690 0,560" fill="url(#front-top)"/>
    <polygon points="0,520 260,650 520,520 520,560 260,690 0,560" fill="var(--green-light)"/>
    <polygon points="260,140 490,273 490,537 260,670 30,537 30,273" fill="var(--white)"/>
    <polygon points="0,1300 520,1270 520,1372 0,1372" fill="var(--green)"/>
    <polygon points="0,1290 520,1262 520,1272 0,1302" fill="var(--green-light)"/>
  </svg>
  <svg class="layer" width="520" height="1372" viewBox="0 0 520 1372" role="img" aria-label="Photo of a lawn mower cutting a green garden lawn">
    <defs>
      <linearGradient id="lawn-photo" x1="0" y1="0" x2="0" y2="1">
        <stop offset="0" stop-color="#5c8f3b"/>
        <stop offset=".5" stop-color="#4c8a2e"/>
        <stop offset="1" stop-color="#7db548"/>
      </linearGradient>
    </defs>
    <polygon points="260,165 468,285 468,525 260,645 52,525 52,285" fill="url(#lawn-photo)"/>
  </svg>
  <div class="front__brand"><span class="front__brand-dot"></span><span class="front__brand-name">GreenCore</span></div>
  <div class="front__headline">
    <div class="front__make">Make</div>
    <div class="front__garden">Your Garden</div>
    <div class="front__paradise">Like Paradise</div>
  </div>
  <div class="call-pill">Call us now</div>
  <div class="phone">0123456789</div>
</section>

<section class="hanger hanger--back">
  <div class="back__photo" role="img" aria-label="Photo of a close-up green lawn with a hand touching the grass"></div>
  <div class="hanger__hole"></div>
  <h2 class="back__title">Benefits of core aeration</h2>
  <ul class="benefits">
    <li><svg viewBox="0 0 28 28"><circle cx="14" cy="14" r="12" fill="none" stroke="#fff" stroke-width="2"/><path d="M8 14.5l4 4 8-9" fill="none" stroke="#fff" stroke-width="2.6" stroke-linecap="round" stroke-linejoin="round"/></svg>Improved air exchange between the soil and atmosphere</li>
    <li><svg viewBox="0 0 28 28"><circle cx="14" cy="14" r="12" fill="none" stroke="#fff" stroke-width="2"/><path d="M8 14.5l4 4 8-9" fill="none" stroke="#fff" stroke-width="2.6" stroke-linecap="round" stroke-linejoin="round"/></svg>Enhanced soil water uptake</li>
    <li><svg viewBox="0 0 28 28"><circle cx="14" cy="14" r="12" fill="none" stroke="#fff" stroke-width="2"/><path d="M8 14.5l4 4 8-9" fill="none" stroke="#fff" stroke-width="2.6" stroke-linecap="round" stroke-linejoin="round"/></svg>Improved fertilizer uptake and use</li>
    <li><svg viewBox="0 0 28 28"><circle cx="14" cy="14" r="12" fill="none" stroke="#fff" stroke-width="2"/><path d="M8 14.5l4 4 8-9" fill="none" stroke="#fff" stroke-width="2.6" stroke-linecap="round" stroke-linejoin="round"/></svg>Reduced water runoff and puddling</li>
    <li><svg viewBox="0 0 28 28"><circle cx="14" cy="14" r="12" fill="none" stroke="#fff" stroke-width="2"/><path d="M8 14.5l4 4 8-9" fill="none" stroke="#fff" stroke-width="2.6" stroke-linecap="round" stroke-linejoin="round"/></svg>Stronger turfgrass roots</li>
    <li><svg viewBox="0 0 28 28"><circle cx="14" cy="14" r="12" fill="none" stroke="#fff" stroke-width="2"/><path d="M8 14.5l4 4 8-9" fill="none" stroke="#fff" stroke-width="2.6" stroke-linecap="round" stroke-linejoin="round"/></svg>Reduced soil compaction</li>
  </ul>
  <div class="back__prompt">
    <div class="back__prompt-lead">Please fill this form to get a</div>
    <div class="back__prompt-strong">Free estimate quote</div>
  </div>
  <div class="form-box">
    <div class="form-row"><span>First name</span><i></i></div>
    <div class="form-row"><span>Last name</span><i></i></div>
    <div class="form-row"><span>Ph no</span><i></i></div>
    <div class="form-row"><span>Email</span><i></i></div>
    <div class="form-row"><span>Address</span><i></i></div>
    <div class="form-row"><span>Sq ft</span><i></i></div>
  </div>
  <div class="call-pill">Call us now</div>
  <div class="phone">0123456789</div>
  <div class="back__band"></div>
</section>

</body>
</html>
```